Flyer for a Business Consultant

I need a one-page description of services. I am a Brennick Certifed Talents Mentor. I do not have a personal website but think I will soon purchase this template https://varlowskins.example/skins/lectern/. I like the larger font, simplicity and larger font. I will attach his pricing flyer which I like - not to overly guide or restrict your creative thinking, but only to give a little perspective. I don't like busy, noisy - I like clarity, simplicity. Here 's the Brennick website which these same traits https://www.brennicktalentshub.example/ and can be a source of ideas and colors.

Target Market(s)

CEOs and Middle Managers in organizations

Industry/Entity Type

Financial Service

Colors

Designer to choose colors to be used in the design.

Requirements
Must have
• Clarity, simplicity, but also strength (not weak or frilly looking)
Nice to have
• Warm color(s), larger/not skinny font
Should not have
• Loud, noisy, busy

```html
<!DOCTYPE html>
<html lang="en">
<head>
<meta charset="utf-8">
<title>Strength-Based Team Effectiveness Flyer</title>
<link rel="stylesheet" href="https://fonts.googleapis.com/css2?family=Open+Sans:ital,wght@0,400;0,600;0,700;0,800;1,400&display=swap">
<style>
:root{
  --stage:#d6d6d4;
  --paper:#ffffff;
  --brand-red:#b32733;
  --pill-red:#d1202f;
  --amber:#f8a51d;
  --flame-start:#e8432a;
  --flame-end:#f05f2a;
  --fold:#9a1d27;
  --ink:#222222;
  --rule:#9a9a9a;
  --badge-fill:#e4e4e4;
  --badge-line:#b8b8b8;
}
*{margin:0;padding:0;box-sizing:border-box}
html,body{width:937px;height:1200px;overflow:hidden;background:var(--stage)}
body{position:relative;font-family:"Open Sans",Arial,sans-serif}
.flyer{position:absolute;left:64px;top:77px;width:809px;height:1046px;background:var(--paper);overflow:hidden}
.flyer-backdrop{position:absolute;inset:0;background:linear-gradient(180deg,#d9d9da 0%,#e6e6e7 55%,#f2f2f2 85%,#ffffff 95%)}
.headline{position:absolute;left:0;right:0;top:78px;text-align:center;color:var(--brand-red);font-weight:800;line-height:1;letter-spacing:-.2px}
.headline .lead{display:block;font-size:33.5px}
.headline .main{display:block;font-size:42.5px;margin-top:6px}
.intro{position:absolute;left:115px;right:136px;top:196px;height:30px}
.intro::before{content:"";position:absolute;left:0;right:0;top:15px;border-top:1px solid var(--rule)}
.intro-pill{position:relative;display:block;width:334px;height:30px;margin:0 auto;background:var(--pill-red);color:#fff;border-radius:9px;font-size:18px;font-weight:700;text-align:center;line-height:30px}
.benefit{position:absolute;top:245px;display:flex;gap:12px}
.benefit-icon{width:77px;height:77px;border-radius:8px;flex:none}
.benefit p{font-size:12px;font-weight:700;color:var(--ink);line-height:14.5px;letter-spacing:-.3px;padding-top:3px}
.b1{left:76px}.b1 .benefit-icon{background:#f7a823}.b1 p{width:115px}
.b2{left:331px}.b2 .benefit-icon{background:#f28a25}.b2 p{width:96px;padding-top:0}
.b3{left:561px}.b3 .benefit-icon{background:#f26f27}.b3 p{width:112px;padding-top:6px}
.service{position:absolute;color:#fff;text-align:center}
.service h2{font-size:19.5px;font-weight:700;margin-bottom:8px}
.service p{font-size:14px;font-weight:600;line-height:20px;letter-spacing:-.25px}
.individual{left:99px;top:370px;width:617px;height:173px;background:var(--amber);padding:31px 36px 0}
.workshop{left:65px;top:543px;width:684px;height:170px;background:linear-gradient(90deg,var(--flame-start),var(--flame-end) 50%,var(--flame-start));padding:23px 60px 0;z-index:2}
.fold{position:absolute;top:713px;z-index:1}
.fold-left{left:65px}
.fold-right{left:716px}
.followon{left:99px;top:713px;width:617px;height:185px;background:var(--amber);padding:27px 40px 0}
.followon h2{margin-bottom:6px}
.contact{position:absolute;left:0;right:0;top:952px;height:70px}
.credential{position:absolute;left:40px;top:0;width:247px;height:68px;border:1px solid var(--badge-line);background:var(--badge-fill)}
.coach{position:absolute;left:317px;top:14px;width:208px;text-align:center}
.coach-name{font-size:21px;font-weight:700;color:var(--brand-red);line-height:24px}
.coach-title{font-size:11px;font-style:italic;color:var(--ink);margin-top:2px}
.contact-divider{position:absolute;left:550px;top:6px;height:47px;border-left:1.5px solid var(--ink)}
.reach{position:absolute;left:570px;top:14px;width:175px;text-align:center;color:var(--ink)}
.reach-phone{font-size:18px;line-height:22px}
.reach-email{font-size:12.5px;font-weight:700;margin-top:3px}
</style>
</head>
<body>
<main class="flyer">
  <div class="flyer-backdrop" role="img" aria-label="Faint grey-toned background photograph of a smiling team huddled together"></div>

  <h1 class="headline"><span class="lead">A STRENGTH-BASED APPROACH TO</span><span class="main">MANAGING TEAM EFFECTIVENESS</span></h1>

  <div class="intro"><span class="intro-pill">We help teams grow stronger by</span></div>

  <div class="benefit b1"><div class="benefit-icon" role="img" aria-label="Icon of clasped hands"></div><p>Bringing a deep awareness of their strengths and the strengths of their associates.</p></div>
  <div class="benefit b2"><div class="benefit-icon" role="img" aria-label="Icon of two people talking"></div><p>Increasing the Team’s communication and sense of partnership.</p></div>
  <div class="benefit b3"><div class="benefit-icon" role="img" aria-label="Icon of a group of employees"></div><p>Improving employee engagement and effectiveness.</p></div>

  <section class="service individual">
    <h2>INDIVIDUAL SESSIONS</h2>
    <p>Conversational feedback and coaching sessions based on Brennick’s TalentPath assessments. These sessions last about an hour and lead to a personalized translation of the results and how their strengths show up in their work and inherent blind spots they bring.</p>
  </section>

  <section class="service workshop">
    <h2>STRENGTH DISCOVERY WORKSHOP</h2>
    <p>A retreat-style Team Workshop in which the team learns each other’s unique Top 5 strengths. The session is very interactive and provides a common language that leads to improved communication and effectiveness. Tailored in 2.3.and 4-hour options are tailored to your Team’s challenges and opportunities.</p>
  </section>
  <svg class="fold fold-left" width="34" height="30" viewBox="0 0 34 30" aria-hidden="true"><polygon points="0,0 34,0 34,30" fill="var(--fold)"/></svg>
  <svg class="fold fold-right" width="33" height="30" viewBox="0 0 33 30" aria-hidden="true"><polygon points="0,0 33,0 0,30" fill="var(--fold)"/></svg>

  <section class="service followon">
    <h2>FOLLOW-ON MODULES</h2>
    <p>Follow-on is important to make the insights learned to be practical and integrated into the Teams’ approach and workflows.<br>In a debrief session included as part of the workshop, we provide several<br>15-minute exercise modules for use in regular meetings, and we offer guest facilitated modules of 30- 60 minutes each.</p>
  </section>

  <footer class="contact">
    <div class="credential" role="img" aria-label="Certification badge"></div>
    <div class="coach"><div class="coach-name">Dorian Halvorsen</div><div class="coach-title">Brennick Workplace Talents Mentor</div></div>
    <div class="contact-divider"></div>
    <div class="reach"><div class="reach-phone">555-014-2738</div><div class="reach-email">dorian@talentsmark.example</div></div>
  </footer>
</main>
</body>
</html>
```